Steady Harbour Coaching Business Card

We need a business card for a new business based in Sydney Australia called "Steady Harbour Coaching". The business provides the following:
1. Resilience systems for individuals - Developing personalised resilience programs that increase stress tolerance, improve work effectiveness and minimise stress responses to challenge.
2. Group Resilience Training for Leaders and managers - Delivering Resilience training packages and ongoing support to leadership cadres within organisations.
3. High Risk Resilience Training - providing resilience training for High Risk professions such as emergency responders, military and police.

Target Market(s)

Corporate / Military / Emergency Responders

Industry/Entity Type

Leadership

Contact Information for Business Card

Steady Harbour Coaching, Rowan Petrakis, 7/18 Wexley St Dunmore 2093, quiet.tide.notes@mailvane.net, www.steadyharbourcoaching.net.au, M# 0471635082
Personalised Mental Resilience Systems for leaders and high risk professions

Requirements
Must have
• 1. Creation of a logo/graphic - to include 3 elements:
a. Military
b.Corporate
c. Emergency Responder.

As long as those 3 elements are included - I am open to any potential designs. Preference given to those who can create a logo out of the above three elements.

```html
<!DOCTYPE html>
<html lang="en">
<head>
<meta charset="utf-8">
<title>Steady Harbour Coaching – Business Card</title>
<link rel="stylesheet" href="https://fonts.googleapis.com/css2?family=Open+Sans:wght@400;600;700&display=swap">
<style>
  :root {
    --page-bg: #e7e4df;
    --card-dark: #161616;
    --card-mid: #3d3d3d;
    --card-light: #5a5a5a;
    --text-light: #f2f2f2;
    --text-soft: #d9d9d9;
    --band-top: #e4e4e4;
    --band-bottom: #a8a8a8;
    --band-text: #3a3a3a;
    --mark-fill: #e9e9e9;
  }
  * { margin: 0; padding: 0; box-sizing: border-box; }
  html, body {
    width: 1200px;
    height: 1022px;
    overflow: hidden;
    background: var(--page-bg);
    font-family: "Open Sans", Arial, sans-serif;
  }
  .card {
    position: absolute;
    left: 100px;
    top: 226px;
    width: 1000px;
    height: 570px;
    border-radius: 6px;
    overflow: hidden;
    background:
      radial-gradient(ellipse at 30% 35%, var(--card-light) 0%, var(--card-mid) 35%, var(--card-dark) 85%);
    color: var(--text-light);
    box-shadow: 0 10px 30px rgba(0,0,0,0.25);
  }
  .holder-name {
    position: absolute;
    right: 60px;
    top: 36px;
    font-size: 40px;
    font-weight: 700;
    line-height: 1.2;
    color: var(--text-soft);
  }
  .brand {
    position: absolute;
    left: 60px;
    top: 110px;
    display: flex;
    align-items: center;
    gap: 32px;
  }
  .brand-mark {
    width: 140px;
    height: 140px;
    background: var(--mark-fill);
    opacity: 0.85;
  }
  .brand-name {
    font-size: 40px;
    font-weight: 600;
    line-height: 1.2;
    text-align: center;
    color: var(--text-light);
  }
  .contact {
    position: absolute;
    list-style: none;
    font-size: 24px;
    line-height: 1.3;
    color: var(--text-soft);
    white-space: nowrap;
  }
  .contact li {
    display: flex;
    align-items: center;
    gap: 12px;
    margin-bottom: 24px;
  }
  .contact svg { width: 26px; height: 26px; flex: none; fill: var(--text-soft); }
  .contact-left { left: 60px; top: 330px; }
  .contact-right { left: 500px; top: 290px; }
  .tagline-band {
    position: absolute;
    left: 0;
    bottom: 0;
    width: 100%;
    height: 86px;
    background: linear-gradient(to bottom, var(--band-top), var(--band-bottom));
    display: flex;
    align-items: center;
    justify-content: center;
    font-size: 25px;
    color: var(--band-text);
    white-space: nowrap;
  }
</style>
</head>
<body>
  <div class="card">
    <div class="holder-name">Rowan Petrakis</div>

    <div class="brand">
      <div class="brand-mark" role="img" aria-label="Brand emblem area"></div>
      <div class="brand-name">Steady Harbour<br>Coaching</div>
    </div>

    <ul class="contact contact-left">
      <li>
        <svg viewBox="0 0 24 24" aria-hidden="true"><path d="M12 2a7 7 0 0 0-7 7c0 5 7 13 7 13s7-8 7-13a7 7 0 0 0-7-7zm0 9.5A2.5 2.5 0 1 1 12 6.5a2.5 2.5 0 0 1 0 5z"/></svg>
        <span>7/18 Wexley St Dunmore 2093,</span>
      </li>
      <li>
        <svg viewBox="0 0 24 24" aria-hidden="true"><path d="M6.6 10.8a15 15 0 0 0 6.6 6.6l2.2-2.2a1 1 0 0 1 1-.25 11.4 11.4 0 0 0 3.6.57 1 1 0 0 1 1 1V20a1 1 0 0 1-1 1A17 17 0 0 1 3 4a1 1 0 0 1 1-1h3.5a1 1 0 0 1 1 1c0 1.25.2 2.45.57 3.57a1 1 0 0 1-.25 1z"/></svg>
        <span>0471635082</span>
      </li>
    </ul>

    <ul class="contact contact-right">
      <li>
        <svg viewBox="0 0 24 24" aria-hidden="true"><path d="M2 5h20v2l-10 6L2 7zM2 9l10 6 10-6v10H2z"/></svg>
        <span>quiet.tide.notes@mailvane.net</span>
      </li>
      <li>
        <svg viewBox="0 0 24 24" aria-hidden="true"><path d="M12 2a10 10 0 1 0 0 20 10 10 0 0 0 0-20zm0 2c.9 0 2.2 1.8 2.8 5H9.2C9.8 5.8 11.1 4 12 4zM4.3 11h3.8a20 20 0 0 0 0 2H4.3a8 8 0 0 1 0-2zm5 2a18 18 0 0 1 0-2h5.4a18 18 0 0 1 0 2zm6.6 0a20 20 0 0 0 0-2h3.8a8 8 0 0 1 0 2zM12 20c-.9 0-2.2-1.8-2.8-5h5.6c-.6 3.2-1.9 5-2.8 5z"/></svg>
        <span>www.steadyharbourcoaching.net.au</span>
      </li>
    </ul>

    <div class="tagline-band">Personalised Mental Resilience Systems for Leaders and High Risk Professions</div>
  </div>
</body>
</html>
```